A4 Pages

We are looking for some title pages for a children journal, we like the designs attached with use of photos and design elements particularly angles and shapes, we like drawings, icons and photos incroprated but not cartoon like.
Some photos attached to work with

Page 1)
Maple & Dove logo
incorporate the image with the MDL letters and rainbow

wording
My Learning Journal
2026
have a blank box to write the child's
have a name box

Page 2
wording
Dove pathway curriculum
Include the logos in the Dove Pathwey curriculum

```html
<!DOCTYPE html>
<html lang="en">
<head>
<meta charset="utf-8">
<title>Maple &amp; Dove – Learning Journal Title Pages</title>
<link rel="stylesheet" href="https://fonts.googleapis.com/css2?family=Chewy&family=Great+Vibes&family=Poppins:wght@500;700&display=swap">
<style>
  :root {
    --stage: #f8981c;
    --sky: #3aa3e3;
    --sky-deep: #2585d4;
    --navy: #1d5e9e;
    --mist: #d8d9db;
    --white: #ffffff;
    --signal-red: #e8302a;
    --sun: #f6d21c;
    --sand: #d79b45;
  }
  * { box-sizing: border-box; margin: 0; padding: 0; }
  html, body { width: 1200px; height: 844px; overflow: hidden; }
  body { background: var(--stage); position: relative; font-family: "Poppins", sans-serif; }

  .page { position: absolute; top: 72px; width: 495px; height: 700px; overflow: hidden; }
  .page--curriculum { left: 75px; background: var(--mist); }
  .page--journal { left: 630px; background: var(--sky); }

  /* Curriculum page */
  .curriculum-backdrop { position: absolute; inset: 0; }
  .curriculum-title {
    position: absolute; left: -118px; top: 300px; width: 330px;
    transform: rotate(-90deg); font-family: "Great Vibes", cursive;
    color: var(--sky-deep); font-size: 46px; line-height: 0.95; text-align: center;
  }
  .pillar { position: absolute; display: flex; align-items: center; gap: 22px; }
  .pillar__badge {
    width: 96px; height: 96px; border-radius: 50%;
    background: var(--white); border: 5px solid var(--sky-deep);
    box-shadow: 0 0 0 4px var(--white); display: grid; place-items: center;
  }
  .pillar__art { width: 70px; height: 70px; border-radius: 50%; }
  .pillar__label { font-family: "Great Vibes", cursive; color: var(--white); font-size: 30px; }
  .pillar--smart { left: 168px; top: 50px; }
  .pillar--inspired { left: 172px; top: 175px; }
  .pillar--unite { left: 160px; top: 300px; }
  .pillar--fit { left: 130px; top: 425px; }
  .pillar--crew { left: 80px; top: 550px; }
  .art-books { background: linear-gradient(135deg, #e94b3c, #f4b63b 40%, #3a8fd0 70%, #4fae5a); }
  .art-arts { background: linear-gradient(135deg, #f3c542, #e87b2f 60%, #2a6fbf); }
  .art-hands { background: linear-gradient(135deg, #f2cd47, #ec8a3a); }
  .art-heart { background: radial-gradient(circle at 45% 40%, #e5342c 55%, #f1d04a); }
  .art-crew { background: conic-gradient(#e5342c 0 33%, #4fae5a 0 66%, #f2cd47 0); }
  .site-pill {
    position: absolute; left: 230px; top: 612px; padding: 8px 22px;
    background: var(--sand); border-radius: 24px; color: var(--white);
    font-weight: 500; font-size: 17px;
  }

  /* Journal page */
  .journal-backdrop { position: absolute; inset: 0; }
  .journal-photo {
    position: absolute; left: 0; top: 0; width: 268px; height: 250px;
    background: linear-gradient(160deg, #e9d8c0, #c79a6a 55%, #8f6a48);
    border-bottom-right-radius: 150px; border: 8px solid var(--white);
    border-top: 0; border-left: 0;
  }
  .brand { position: absolute; right: 22px; top: 48px; display: flex; flex-direction: column; align-items: center; gap: 8px; }
  .brand__mark { width: 46px; height: 46px; border-radius: 50%; background: var(--sun); }
  .brand__name { font-family: "Chewy", cursive; color: var(--white); font-size: 30px; line-height: 1; text-align: center; }
  .brand__name span { display: block; font-size: 19px; letter-spacing: 2px; }
  .journal-title {
    position: absolute; left: 48px; top: 272px; font-family: "Chewy", cursive;
    color: var(--white); line-height: 0.9;
  }
  .journal-title__my { font-size: 48px; display: block; }
  .journal-title__main { font-size: 92px; display: block; }
  .journal-title__year { font-size: 46px; display: block; margin-left: 54px; }
  .name-tag { position: absolute; left: 78px; top: 540px; width: 330px; }
  .name-tag__prompt { font-family: "Chewy", cursive; color: var(--signal-red); font-size: 24px; margin-left: 30px; }
  .name-tag__field {
    margin-top: 6px; height: 78px; background: var(--white); border-radius: 40px;
    position: relative;
  }
  .name-tag__field::after {
    content: ""; position: absolute; left: 28px; right: 28px; bottom: 22px;
    height: 3px; background: var(--signal-red);
  }
</style>
</head>
<body>

<section class="page page--curriculum" aria-label="Dove Pathway Curriculum title page">
  <svg class="curriculum-backdrop" viewBox="0 0 495 700" aria-hidden="true">
    <path d="M150 0 H495 V700 H40 C90 620 120 560 130 480 C140 380 110 300 150 200 C175 130 140 60 150 0Z" fill="var(--sky-deep)"/>
    <path d="M300 380 C380 330 460 380 495 360 V700 H200 C260 620 220 470 300 380Z" fill="var(--navy)" opacity="0.45"/>
    <path d="M400 640 L480 610 L495 700 L420 700Z" fill="var(--signal-red)"/>
    <g fill="var(--white)">
      <circle cx="300" cy="680" r="4"/><circle cx="318" cy="676" r="5"/>
      <circle cx="338" cy="672" r="6"/><circle cx="360" cy="668" r="7"/>
    </g>
  </svg>

  <h1 class="curriculum-title">Dove Pathway<br>Curriculum</h1>

  <div class="pillar pillar--smart"><div class="pillar__badge"><div class="pillar__art art-books" role="img" aria-label="Stack of colourful books"></div></div><span class="pillar__label">Smart Start</span></div>
  <div class="pillar pillar--inspired"><div class="pillar__badge"><div class="pillar__art art-arts" role="img" aria-label="Paint palette with brush and music note"></div></div><span class="pillar__label">Inspired</span></div>
  <div class="pillar pillar--unite"><div class="pillar__badge"><div class="pillar__art art-hands" role="img" aria-label="Two hands forming a heart"></div></div><span class="pillar__label">Unite</span></div>
  <div class="pillar pillar--fit"><div class="pillar__badge"><div class="pillar__art art-heart" role="img" aria-label="Heart with pulse line and ball"></div></div><span class="pillar__label">Fit</span></div>
  <div class="pillar pillar--crew"><div class="pillar__badge"><div class="pillar__art art-crew" role="img" aria-label="Circle of figures holding hands"></div></div><span class="pillar__label">Crew</span></div>

  <div class="site-pill">mapledove.school</div>
</section>

<section class="page page--journal" aria-label="My Learning Journal 2026 title page">
  <svg class="journal-backdrop" viewBox="0 0 495 700" aria-hidden="true">
    <path d="M0 300 C120 250 260 330 380 300 C440 285 480 300 495 310 V470 C420 520 300 430 180 500 C100 545 40 520 0 540Z" fill="var(--sky-deep)"/>
    <path d="M0 610 L95 570 L110 700 L0 700Z" fill="var(--signal-red)"/>
    <g fill="var(--white)">
      <circle cx="20" cy="672" r="5"/><circle cx="38" cy="676" r="6"/>
      <circle cx="58" cy="680" r="7"/><circle cx="80" cy="684" r="6"/>
    </g>
  </svg>

  <div class="journal-photo" role="img" aria-label="Wooden peg board with a rainbow of beads and the letters MDL in a classroom"></div>

  <div class="brand">
    <div class="brand__mark"></div>
    <div class="brand__name">Maple &amp; Dove<span>kindergarten</span></div>
  </div>

  <h2 class="journal-title">
    <span class="journal-title__my">My</span>
    <span class="journal-title__main">Learning</span>
    <span class="journal-title__main">Journal</span>
    <span class="journal-title__year">2026</span>
  </h2>

  <div class="name-tag">
    <p class="name-tag__prompt">Hi! My name is</p>
    <div class="name-tag__field"></div>
  </div>
</section>

</body>
</html>
```